KMR Business cards

I currently have a logo that was designed by a pixel harbor designer. I would like this to be added to the business card.

We are an innovative new start-up business offering finance solutions to the car dealership market in the UK. So our clients are quiet traditional, so are cards need to fit in, but at the same time show we are a modern online business.

Finance

```html
<!DOCTYPE html>
<html lang="en">
<head>
<meta charset="utf-8">
<title>KMR Business Cards</title>
<link rel="stylesheet" href="https://fonts.googleapis.com/css2?family=Didact+Gothic&family=Montserrat:wght@700&display=swap">
<style>
  :root {
    --backdrop: #e9e7e3;
    --navy-deep: #163a63;
    --navy-light: #2a5f8f;
    --ink: #1f3357;
    --paper: #ffffff;
    --muted: #5a6a80;
    --arc: #e3e7ec;
    --on-navy: #ffffff;
  }
  * { box-sizing: border-box; margin: 0; padding: 0; }
  html, body { width: 1200px; height: 800px; overflow: hidden; }
  body {
    background: var(--backdrop);
    font-family: "Didact Gothic", "Century Gothic", sans-serif;
    position: relative;
  }
  .card {
    position: absolute;
    top: 235px;
    width: 510px;
    height: 330px;
    box-shadow: 0 6px 18px rgba(0,0,0,0.18);
    overflow: hidden;
  }
  /* Reverse side */
  .card--back {
    left: 60px;
    background: radial-gradient(ellipse at 50% 40%, var(--navy-light), var(--navy-deep) 80%);
    color: var(--on-navy);
    text-align: center;
  }
  .card--back .tagline {
    position: absolute; top: 44px; left: 0; right: 0;
    font-size: 26px; letter-spacing: 0.5px;
  }
  .card--back .brand {
    position: absolute; top: 118px; left: 0; right: 0;
    display: flex; justify-content: center; align-items: center; gap: 16px;
  }
  .card--back .web {
    position: absolute; bottom: 34px; left: 0; right: 0;
    font-size: 17px; letter-spacing: 0.5px;
  }
  .brand-mark {
    width: 70px; height: 70px; border-radius: 50%;
    border: 4px solid currentColor; flex: none;
  }
  .brand-name {
    font-size: 24px; line-height: 1.05; text-align: left;
  }
  /* Front side */
  .card--front {
    left: 630px;
    background: var(--paper);
    color: var(--ink);
  }
  .card--front .arcs {
    position: absolute; right: -120px; top: 60px;
    width: 380px; height: 380px;
  }
  .card--front .brand {
    position: absolute; top: 30px; left: 34px;
    display: flex; align-items: center; gap: 14px;
  }
  .card--front .brand-mark { width: 60px; height: 60px; }
  .card--front .brand-name { font-size: 21px; }
  .person {
    position: absolute; top: 150px; right: 40px; text-align: right;
  }
  .person-name {
    font-family: "Montserrat", sans-serif; font-weight: 700;
    font-size: 21px; letter-spacing: 1px;
  }
  .person-role { font-size: 15px; color: var(--muted); margin-top: 4px; }
  .contacts {
    position: absolute; left: 34px; bottom: 30px;
    list-style: none; font-size: 14px; color: var(--ink);
  }
  .contacts li { display: flex; align-items: center; gap: 9px; margin-top: 6px; }
  .contacts svg { width: 15px; height: 15px; flex: none; }
</style>
</head>
<body>

  <section class="card card--back">
    <p class="tagline">Drive now, pay later</p>
    <div class="brand">
      <span class="brand-mark"></span>
      <span class="brand-name">KMR<br>Kingsmere<br>Motor Finance</span>
    </div>
    <p class="web">www.kingsmeremotor.com</p>
  </section>

  <section class="card card--front">
    <svg class="arcs" viewBox="0 0 380 380" aria-hidden="true">
      <circle cx="190" cy="190" r="175" fill="none" stroke="var(--arc)" stroke-width="14"/>
      <circle cx="190" cy="190" r="150" fill="none" stroke="var(--arc)" stroke-width="4"/>
    </svg>
    <div class="brand">
      <span class="brand-mark"></span>
      <span class="brand-name">KMR<br>Kingsmere<br>Motor Finance</span>
    </div>
    <div class="person">
      <p class="person-name">DANIEL PORTER</p>
      <p class="person-role">Founder</p>
    </div>
    <ul class="contacts">
      <li>
        <svg viewBox="0 0 16 16" aria-hidden="true"><circle cx="8" cy="8" r="8" fill="var(--ink)"/><path d="M5 4.5c.6-.4 1.1-.2 1.4.4l.5 1c.2.4 0 .8-.3 1l-.4.3c.5 1 1.2 1.7 2.1 2.1l.3-.4c.3-.3.7-.5 1-.3l1 .5c.6.3.8.8.4 1.4-.5.8-1.4 1-2.3.6C6.8 10.3 5.7 9.2 4.9 7.3c-.4-.9-.2-1.9.1-2.8z" fill="#fff"/></svg>
        07700 900418
      </li>
      <li>
        <svg viewBox="0 0 16 16" aria-hidden="true"><circle cx="8" cy="8" r="8" fill="var(--ink)"/></svg>
        daniel.porter_kmr
      </li>
      <li>
        <svg viewBox="0 0 16 16" aria-hidden="true"><circle cx="8" cy="8" r="8" fill="var(--ink)"/><rect x="4" y="5" width="8" height="6" fill="none" stroke="#fff" stroke-width="1"/><path d="M4 5l4 3.5L12 5" fill="none" stroke="#fff" stroke-width="1"/></svg>
        daniel.porter@kingsmeremotor.com
      </li>
    </ul>
  </section>

</body>
</html>
```